Health & Beauty Company- Business Card Design

Two-sided business card design and logo design.

Company markets and sells otc treatments for the health and beauty industry. Marketing products to doctors, pharmacists and retail drug companies like tormundos, pqz and lumo fex.

Designs should be submitted as vector based PDFs. To keep your text in vector format, our printer recommends applications like Adobe Illustrator, Adobe InDesign and more recent versions of Adobe Photoshop.

Target Market(s)

Drug stores, doctors and pharmacists

Industry/Entity Type

Printer

Requirements
Must have
• Back side of business card should include company logo and our tagline: "Advancing Everyday Wellness & Beauty Care"

Company name acronym must be included: QTRM

```html
<!DOCTYPE html>
<html lang="en">
<head>
<meta charset="utf-8">
<title>QTRM Business Card</title>
<link href="https://fonts.googleapis.com/css2?family=Open+Sans:wght@400;600;700&display=swap" rel="stylesheet">
<style>
  :root {
    --stage: #3a3a3a;
    --card-dark: #1f1f1f;
    --card-light-top: #e2e2e2;
    --card-light-bottom: #cfcfcf;
    --ink-light: #f2f2f2;
    --ink-muted: #cfcfcf;
    --ink-dark: #1c1c1c;
    --rule: #6a6a6a;
  }
  * { margin: 0; padding: 0; box-sizing: border-box; }
  html, body { width: 1200px; height: 534px; overflow: hidden; }
  body {
    background: var(--stage);
    font-family: "Open Sans", sans-serif;
    position: relative;
  }
  .card {
    position: absolute;
    top: 119px;
    width: 517px;
    height: 294px;
  }
  .card-front { left: 77px; background: var(--card-dark); color: var(--ink-light); }
  .card-back {
    left: 605px;
    background: linear-gradient(160deg, var(--card-light-top), var(--card-light-bottom));
    color: var(--ink-dark);
  }
  .identity {
    position: absolute;
    left: 0; width: 218px;
    top: 121px;
    text-align: center;
  }
  .identity-name { font-size: 17px; font-weight: 600; line-height: 22px; }
  .identity-title { font-size: 9px; color: var(--ink-muted); line-height: 12px; }
  .identity-address { font-size: 9px; color: var(--ink-muted); margin-top: 10px; }
  .divider {
    position: absolute;
    left: 218px; top: 117px;
    width: 1px; height: 61px;
    background: var(--rule);
  }
  .contact-list {
    position: absolute;
    left: 236px; top: 115px;
    list-style: none;
  }
  .contact-list li {
    display: flex; align-items: center;
    height: 16px;
    font-size: 10px;
    color: var(--ink-light);
  }
  .contact-list svg { width: 11px; height: 11px; margin-right: 7px; fill: var(--ink-light); }
  .brand-mark {
    position: absolute;
    left: 20px; top: 62px;
    width: 112px; height: 112px;
    border: 3px solid var(--ink-dark);
    border-radius: 50%;
  }
  .brand {
    position: absolute;
    left: 176px; top: 111px;
  }
  .brand-name { font-size: 56px; font-weight: 700; line-height: 50px; letter-spacing: 0.5px; }
  .brand-tagline { font-size: 13.5px; font-weight: 700; line-height: 18px; margin-top: 2px; letter-spacing: -0.2px; }
</style>
</head>
<body>
  <section class="card card-front">
    <div class="identity">
      <p class="identity-name">Marisa Holloway</p>
      <p class="identity-title">President &amp; CEO</p>
      <p class="identity-address">48 Linden Row, Cityville, ST 00000</p>
    </div>
    <div class="divider"></div>
    <ul class="contact-list">
      <li><svg viewBox="0 0 12 12"><path d="M2 1l3 0 1 3-1.5 1a7 7 0 0 0 2.5 2.5L8 6l3 1 0 3c-5 0-9-4-9-9z"/></svg>+000-000-0000</li>
      <li><svg viewBox="0 0 12 12"><path d="M3 1h6v3H3zM1 5h10v4H9v2H3V9H1zM4 8v2h4V8z"/></svg>+000-000-0000</li>
      <li><svg viewBox="0 0 12 12"><path d="M1 3h10v7H1zM1.5 3.5L6 7l4.5-3.5" fill="none" stroke="#f2f2f2" stroke-width="1"/></svg>mholloway@qtrm.co</li>
      <li><svg viewBox="0 0 12 12"><circle cx="6" cy="6" r="5"/></svg>marisa.qtrm</li>
    </ul>
  </section>

  <section class="card card-back">
    <div class="brand-mark"></div>
    <div class="brand">
      <h1 class="brand-name">QTRM</h1>
      <p class="brand-tagline">Advancing Everyday Wellness &amp; Beauty Care</p>
    </div>
  </section>
</body>
</html>
```